Parkinson's Disease Progression

Visually describe the rate of Parkinson progression in the first 15 years following diagnosis. Title: "Patient-Perceived Progression of Parkinsonism"

The attached figure names "meanqol" is the curve that should serve as the basis of this graphic. Everything else-- color, labels, font, etc. describe this curve.
Thank you!

Target Market(s)

People with Parkisnon's Disease, neurologists, family members.

Font styles to use
Sans Serif

Requirements
Must have
• Must have the lines going through these exact numbers
Excellent -- 502
Very good- 661
Good- 895
Fair- 1268
Poor- 1655

LABELS:
Title: "Patient-Perceived Progression of Parkinsonism"
"SAW-MX (Self-Assessed Wellbeing Index for Movement Conditions)" should be the label on the left.
"Quality of Life" should be the label on the right
"Years Since Diagnosis" should be the label on the bottom
Nice to have
• A color scheme that goes from GOOD (low numbers) to BAD (high numbers).

Easy to read (elderly)

```html
<!DOCTYPE html>
<html lang="en">
<head>
<meta charset="utf-8">
<title>Patient-Perceived Progression of Parkinsonism</title>
<link rel="stylesheet" href="https://fonts.googleapis.com/css2?family=Barlow+Condensed:wght@300;400;600;700;800&display=swap">
<style>
  :root {
    --ink: #000000;
    --paper: #ffffff;
    --band-red: #ee1c25;
    --band-orange: #f37c20;
    --band-yellow: #f2ea2b;
    --band-lime: #a8cf3b;
    --band-green: #39b54a;
    --band-deep-green: #0f9447;
    --guide: #ffffff;
  }
  html, body {
    margin: 0;
    padding: 0;
    width: 1200px;
    height: 848px;
    overflow: hidden;
    background: var(--paper);
  }
  .chart {
    display: block;
    width: 1200px;
    height: 848px;
  }
  .chart-title {
    font-family: "Barlow Condensed", sans-serif;
    font-weight: 800;
    font-size: 25px;
    letter-spacing: 0.3px;
    fill: var(--ink);
  }
  .axis-title {
    font-family: "Barlow Condensed", sans-serif;
    font-weight: 400;
    font-size: 20px;
    letter-spacing: 0.4px;
    fill: var(--ink);
  }
  .tick-label {
    font-family: "Barlow Condensed", sans-serif;
    font-weight: 600;
    font-size: 14px;
    fill: var(--ink);
  }
  .quality-label {
    font-family: "Barlow Condensed", sans-serif;
    font-weight: 700;
    font-size: 14px;
    fill: var(--ink);
  }
  .quality-tag { fill: var(--paper); }
  .guide-line {
    stroke: var(--guide);
    stroke-width: 1.6;
    stroke-dasharray: 1.5 3;
    opacity: 0.9;
  }
  .axis-line { fill: var(--ink); }
  .mean-curve {
    fill: none;
    stroke: var(--ink);
    stroke-width: 3;
    stroke-linecap: round;
  }
  .confidence-edge {
    fill: none;
    stroke: var(--ink);
    stroke-width: 1;
    stroke-dasharray: 3 2.5;
  }
  .stop-red { stop-color: var(--band-red); }
  .stop-orange { stop-color: var(--band-orange); }
  .stop-yellow { stop-color: var(--band-yellow); }
  .stop-lime { stop-color: var(--band-lime); }
  .stop-green { stop-color: var(--band-green); }
  .stop-deep-green { stop-color: var(--band-deep-green); }
  .stop-glow { stop-color: var(--paper); }
</style>
</head>
<body>
<svg class="chart" viewBox="0 0 850 600" preserveAspectRatio="none" role="img" aria-label="Line chart of patient-perceived progression of parkinsonism over 15 years since diagnosis">
  <defs>
    <linearGradient id="quality-scale" gradientUnits="userSpaceOnUse" x1="0" y1="108" x2="0" y2="483">
      <stop offset="0" class="stop-red"/>
      <stop offset="0.14" class="stop-red"/>
      <stop offset="0.37" class="stop-orange"/>
      <stop offset="0.55" class="stop-yellow"/>
      <stop offset="0.66" class="stop-lime"/>
      <stop offset="0.82" class="stop-green"/>
      <stop offset="1" class="stop-deep-green"/>
    </linearGradient>
    <linearGradient id="confidence-glow" gradientUnits="userSpaceOnUse" x1="190" y1="0" x2="640" y2="0">
      <stop offset="0" class="stop-glow" stop-opacity="0.55"/>
      <stop offset="0.6" class="stop-glow" stop-opacity="0.75"/>
      <stop offset="1" class="stop-glow" stop-opacity="0.15"/>
    </linearGradient>
  </defs>

  <text class="chart-title" x="415" y="70" text-anchor="middle">PATIENT-PERCEIVED PROGRESSION OF PARKINSONISM</text>

  <g class="plot">
    <rect x="190" y="108" width="495" height="376" fill="url(#quality-scale)"/>

    <g class="quality-guides">
      <line class="guide-line" x1="192" y1="201" x2="685" y2="201"/>
      <line class="guide-line" x1="192" y1="287" x2="685" y2="287"/>
      <line class="guide-line" x1="192" y1="341" x2="685" y2="341"/>
      <line class="guide-line" x1="192" y1="378" x2="685" y2="378"/>
    </g>

    <path class="confidence-band" fill="url(#confidence-glow)"
      d="M192,430 L205,369 C235,368 290,325 346,318 S410,316 440,298 S500,257 540,238 S600,222 635,196
         L640,278 C610,268 590,266 540,272 S470,300 440,311 S380,328 346,330 S230,385 205,414 Z"/>
    <path class="confidence-edge" d="M205,369 C235,368 290,325 346,318 S410,316 440,298 S500,257 540,238 S600,224 627,205"/>
    <path class="confidence-edge" d="M205,414 C230,385 290,336 346,330 S410,328 440,311 S500,270 540,272 S600,266 627,272"/>
    <path class="mean-curve" d="M205,392 C240,372 290,330 346,324 S410,322 440,304 S500,262 540,252 S610,244 627,242"/>

    <g class="quality-tags">
      <rect class="quality-tag" x="633" y="178" width="52" height="18"/>
      <text class="quality-label" x="659" y="192" text-anchor="middle">POOR</text>
      <rect class="quality-tag" x="637" y="265" width="48" height="18"/>
      <text class="quality-label" x="661" y="279" text-anchor="middle">FAIR</text>
      <rect class="quality-tag" x="633" y="320" width="52" height="18"/>
      <text class="quality-label" x="659" y="334" text-anchor="middle">GOOD</text>
      <rect class="quality-tag" x="603" y="356" width="82" height="18"/>
      <text class="quality-label" x="644" y="370" text-anchor="middle">VERY GOOD</text>
      <rect class="quality-tag" x="603" y="460" width="82" height="18"/>
      <text class="quality-label" x="644" y="474" text-anchor="middle">EXCELLENT</text>
    </g>

    <rect class="axis-line" x="188" y="108" width="4" height="382"/>
    <rect class="axis-line" x="188" y="481" width="497" height="9"/>
  </g>

  <g class="y-ticks">
    <text class="tick-label" x="173" y="129" text-anchor="end">1600</text>
    <text class="tick-label" x="173" y="175" text-anchor="end">1400</text>
    <text class="tick-label" x="173" y="221" text-anchor="end">1200</text>
    <text class="tick-label" x="173" y="268" text-anchor="end">1000</text>
    <text class="tick-label" x="173" y="314" text-anchor="end">800</text>
    <text class="tick-label" x="173" y="360" text-anchor="end">600</text>
    <text class="tick-label" x="173" y="407" text-anchor="end">400</text>
    <text class="tick-label" x="173" y="453" text-anchor="end">200</text>
  </g>

  <g class="x-ticks">
    <text class="tick-label" x="205" y="522" text-anchor="middle">0</text>
    <text class="tick-label" x="346" y="522" text-anchor="middle">5</text>
    <text class="tick-label" x="487" y="522" text-anchor="middle">10</text>
    <text class="tick-label" x="627" y="522" text-anchor="middle">15</text>
  </g>

  <text class="axis-title" x="430" y="555" text-anchor="middle">YEARS SINCE DIAGNOSIS</text>
  <text class="axis-title" transform="translate(120 300) rotate(-90)" text-anchor="middle">SELF-ASSESSED WELLBEING</text>
  <text class="axis-title" transform="translate(727 298) rotate(-90)" text-anchor="middle">QUALITY OF LIFE</text>
</svg>
</body>
</html>
```